Wine label refresh

We are wanting to modify our Corran Hollow label to include a picture on it.
I have attached the pictures below which we would like on the label. They are of the Corran Hollow vineyard. I have also attached an example of another label with a picture on it that we like the style of.
Updates
Industry/Entity Type
Vineyard
Requirements
Must have
- The Corran Hollow text must stay the same but can be moved down. It still needs to be the same size though.
Marlborough Sauvignon Blanc should remain in the same font and roughly the same size.
Wine of New Zealand also must stay but could potentially be moved.
Nice to have
- It would be nice if we could keep the PM logo on the front label but feel free to experiment with where this goes.

```html
<!DOCTYPE html>
<html lang="en">
<head>
<meta charset="utf-8">
<title>Corran Hollow – Marlborough Sauvignon Blanc Label</title>
<link rel="stylesheet" href="https://fonts.googleapis.com/css2?family=Cormorant+Garamond:wght@500&family=Cormorant+SC:wght@500&family=Pinyon+Script&family=Lato:wght@300&display=swap">
<style>
  :root {
    --paper: #ffffff;
    --bleed-line: #29abe2;
    --trim-line: #231f20;
    --gold: #d69416;
    --estate-brown: #6e3325;
    --varietal-red: #c8102e;
    --detail-grey: #b3aaa2;
    --photo-tone: #a7ae9c;
  }
  * { margin: 0; padding: 0; box-sizing: border-box; }
  html, body {
    width: 1200px;
    height: 1000px;
    overflow: hidden;
    background: var(--paper);
  }
  .canvas {
    position: relative;
    width: 1200px;
    height: 1000px;
    background: var(--paper);
  }
  .bleed-guide {
    position: absolute;
    left: 22px; top: 69px;
    width: 1157px; height: 861px;
    border: 2px solid var(--bleed-line);
    border-radius: 6px;
  }
  .trim-guide {
    position: absolute;
    left: 45px; top: 99px;
    width: 1111px; height: 803px;
    border: 1.5px solid var(--trim-line);
  }
  .label {
    position: absolute;
    left: 68px; top: 123px;
    width: 1064px; height: 756px;
    border: 33px solid var(--gold);
    background: var(--paper);
  }
  .label-inner-rule {
    position: absolute;
    left: 11px; top: 12px;
    right: 11px; bottom: 12px;
    border: 2px solid var(--gold);
  }
  .monogram {
    position: absolute;
    left: 0; right: 0; top: 58px;
    text-align: center;
    font-family: "Cormorant Garamond", serif;
    font-weight: 500;
    font-size: 110px;
    line-height: 1;
    letter-spacing: 2px;
    color: var(--estate-brown);
  }
  .estate-name {
    position: absolute;
    left: 0; right: 0; top: 174px;
    text-align: center;
    font-family: "Cormorant SC", serif;
    font-weight: 500;
    font-size: 51px;
    line-height: 1;
    letter-spacing: 2px;
    color: var(--estate-brown);
  }
  .vineyard-photo {
    position: absolute;
    left: 269px; top: 237px;
    width: 460px; height: 245px;
  }
  .varietal {
    position: absolute;
    left: 0; right: 0; top: 506px;
    text-align: center;
    font-family: "Pinyon Script", cursive;
    font-size: 56px;
    line-height: 1;
    color: var(--varietal-red);
  }
  .vintage {
    position: absolute;
    left: 0; right: 0; top: 556px;
    text-align: center;
    font-family: "Pinyon Script", cursive;
    font-size: 46px;
    line-height: 1;
    color: var(--varietal-red);
  }
  .details {
    position: absolute;
    left: 27px; right: 29px; top: 626px;
    display: flex;
    justify-content: space-between;
    font-family: "Lato", sans-serif;
    font-weight: 300;
    font-size: 40px;
    line-height: 1;
    color: var(--detail-grey);
  }
</style>
</head>
<body>
  <main class="canvas">
    <div class="bleed-guide"></div>
    <div class="trim-guide"></div>

    <section class="label">
      <div class="label-inner-rule"></div>

      <div class="monogram">PM</div>
      <h1 class="estate-name">Corran Hollow</h1>

      <svg class="vineyard-photo" viewBox="0 0 460 245" role="img" aria-label="Oval photograph of the Corran Hollow vineyard with vine rows, a cottage, palm trees and hills">
        <defs>
          <radialGradient id="oval-fade" cx="0.5" cy="0.5" r="0.5">
            <stop offset="0.88" stop-color="#fff" stop-opacity="1"/>
            <stop offset="1" stop-color="#fff" stop-opacity="0"/>
          </radialGradient>
          <mask id="soft-oval">
            <ellipse cx="230" cy="122.5" rx="230" ry="122.5" fill="url(#oval-fade)"/>
          </mask>
        </defs>
        <rect width="460" height="245" fill="var(--photo-tone)" mask="url(#soft-oval)"/>
      </svg>

      <p class="varietal">Marlborough Sauvignon Blanc</p>
      <p class="vintage">2012</p>

      <div class="details">
        <span class="volume">750ml</span>
        <span class="origin">NEW ZEALAND WINE</span>
        <span class="abv">13% alc/vol</span>
      </div>
    </section>
  </main>
</body>
</html>
```